FLOUR BAG DESIGN

• Bag dimensions: H=280 mm, A=105 mm, B=65 mm (look at the picture »dimensions«)
• Bag will be used for different types of flour (wheat flour, corn flour, buckwheat flour, etc.) and porridge (buckwheat, millet, etc. ) so we are looking for universal design that will suit to all of them. Please have in mind that somewhere on the front side (AxH) there needs to be some space for the name of the flour/porridge.
• I also uploaded design of an existing bag just in case you want to see it. Design on the bag represents the mill where our business started. We could say that existing bag is very traditional, we are looking for a little bit more modern style bag but still want to emphasize the link to our tradition.

I forgot to select "10 days " when desribing the label desing I need, before posting the project

• • We would like to integrate our logo (look at the picture »logo«) and text which is also present on the current bag. Front side AxH: Koleškov Mlin (name of the company), Fužina – Zagradec (name of the village), Meljemo že od 1724 (meaning Flour milling since 1682). On the right side: same as on the picture »current bag (dimensions BxH)«.

```html
<!DOCTYPE html>
<html lang="sl">
<head>
<meta charset="utf-8">
<title>Koleškov Mlin – flour bag</title>
<link href="https://fonts.googleapis.com/css2?family=Caveat+Brush&family=Dancing+Script:wght@600&display=swap" rel="stylesheet">
<style>
  :root {
    --paper: #ffffff;
    --bag-top: #fdd283;
    --bag-glow: #fde6a6;
    --brown: #6b3608;
    --brown-dark: #4a2204;
    --orange: #f0a21f;
    --ink: #7a4210;
    --mark: #222;
  }
  html, body {
    margin: 0;
    width: 1200px;
    height: 1200px;
    overflow: hidden;
    background: var(--paper);
  }
  .canvas {
    position: relative;
    width: 1200px;
    height: 1200px;
  }
  .bag-front {
    position: absolute;
    left: 408px;
    top: 0;
    width: 384px;
    height: 1200px;
    overflow: hidden;
    background:
      radial-gradient(ellipse 320px 420px at 50% 74%, var(--bag-glow) 0%, rgba(253,230,166,0.6) 55%, rgba(253,210,131,0) 100%),
      var(--bag-top);
  }
  .brand-mark {
    position: absolute;
    left: 0;
    right: 0;
    top: 548px;
    text-align: center;
    font-family: "Caveat Brush", cursive;
    color: var(--ink);
  }
  .brand-mark__dot {
    display: block;
    width: 22px;
    height: 22px;
    margin: 0 auto 4px;
    border-radius: 50%;
    background: var(--ink);
  }
  .brand-mark__name {
    font-size: 11px;
    line-height: 1;
  }
  .brand-mark__note {
    font-family: sans-serif;
    font-size: 5px;
    margin-top: 3px;
  }
  .band {
    position: absolute;
    left: 0;
    width: 100%;
  }
  .band--line-top { top: 699px; height: 7px; background: var(--orange); }
  .band--stripe {
    top: 716px;
    height: 178px;
    background: repeating-linear-gradient(90deg, var(--brown) 0 3px, #5e2e06 3px 6px);
  }
  .band--line-bottom { top: 903px; height: 7px; background: var(--orange); }
  .medallion {
    position: absolute;
    left: 40px;
    top: 652px;
    width: 312px;
    height: 312px;
    border-radius: 50%;
    background: var(--brown-dark);
    box-shadow: 0 6px 16px rgba(80,40,0,0.35);
  }
  .medallion__ring {
    position: absolute;
    inset: 6px;
    border-radius: 50%;
    border: 3px solid var(--orange);
  }
  .medallion__scene {
    position: absolute;
    inset: 13px;
    border-radius: 50%;
    background: radial-gradient(circle at 45% 40%, #8a5120 0%, #5d2d08 60%, #4a2204 100%);
  }
  .arched-type {
    position: absolute;
    left: 0;
    top: 0;
    width: 384px;
    height: 1200px;
  }
  .title, .years {
    font-family: "Caveat Brush", cursive;
    fill: var(--ink);
  }
  .title { font-size: 38px; letter-spacing: 2px; }
  .years { font-size: 50px; letter-spacing: 2px; fill: var(--brown); }
  .village {
    position: absolute;
    left: 0; right: 0;
    top: 1036px;
    text-align: center;
    font-family: "Caveat Brush", cursive;
    font-size: 23px;
    color: var(--ink);
  }
  .tagline {
    position: absolute;
    left: 0; right: 0;
    top: 1074px;
    text-align: center;
    font-family: "Dancing Script", cursive;
    font-weight: 600;
    font-size: 20px;
    color: var(--ink);
  }
  .crop-marks {
    position: absolute;
    left: 0; top: 0;
    width: 1200px; height: 1200px;
  }
  .crop-marks line { stroke: var(--mark); stroke-width: 1; }
</style>
</head>
<body>
<div class="canvas">
  <section class="bag-front">
    <div class="brand-mark">
      <span class="brand-mark__dot"></span>
      <div class="brand-mark__name">Koleškov mlin</div>
      <div class="brand-mark__note">moka iz kamnitega mlina</div>
    </div>

    <div class="band band--line-top"></div>
    <div class="band band--stripe"></div>
    <div class="band band--line-bottom"></div>

    <div class="medallion">
      <div class="medallion__ring"></div>
      <div class="medallion__scene" role="img" aria-label="Sketch of the old mill buildings by the river, with bread, pretzel and wheat ears"></div>
    </div>

    <svg class="arched-type" viewBox="0 0 384 1200">
      <defs>
        <path id="title-arc" d="M 40 656 Q 196 604 352 656"/>
        <path id="years-arc" d="M 20 930 Q 196 1070 364 930"/>
      </defs>
      <text class="title"><textPath href="#title-arc" startOffset="50%" text-anchor="middle">KOLEŠKOV MLIN</textPath></text>
      <text class="years"><textPath href="#years-arc" startOffset="50%" text-anchor="middle">XXXX - XXXX</textPath></text>
    </svg>

    <div class="village">LIPOVEC - PODBREG</div>
    <div class="tagline">Meljemo že od 1724</div>
  </section>

  <svg class="crop-marks" viewBox="0 0 1200 1200" aria-hidden="true">
    <line x1="437" y1="0" x2="437" y2="20"/>
    <line x1="408" y1="31" x2="428" y2="31"/>
    <line x1="763" y1="0" x2="763" y2="20"/>
    <line x1="772" y1="31" x2="792" y2="31"/>
    <line x1="437" y1="1180" x2="437" y2="1200"/>
    <line x1="408" y1="1169" x2="428" y2="1169"/>
    <line x1="763" y1="1180" x2="763" y2="1200"/>
    <line x1="772" y1="1169" x2="792" y2="1169"/>
  </svg>
</div>
</body>
</html>
```